Vellmore Quadrant Systems LLC
Elevate Your Workflow
Vellmore Quadrant Systems LLC - Information Technology
Creative Brief
Corporate
Dorian Feltcher
President
Brennick, VA
dorian@vellmore-quadrant.example
www.vellmore-quadrant.example
Elevate Your Workflow www.vellmore-quadrant.example

```html
<!DOCTYPE html>
<html lang="en">
<head>
<meta charset="utf-8">
<title>Vellmore Quadrant Systems LLC — Stationery</title>
<link href="https://fonts.googleapis.com/css2?family=Arimo:wght@400;700&display=swap" rel="stylesheet">
<style>
  :root {
    --backdrop: #ece7df;
    --paper: #ffffff;
    --ink: #2b2b2b;
    --ink-soft: #555b60;
    --brand-blue: #1ea9d3;
    --brand-blue-deep: #0d8fbb;
    --brand-blue-pale: #d6f0f8;
  }
  * { box-sizing: border-box; margin: 0; padding: 0; }
  html, body { width: 1200px; height: 846px; overflow: hidden; }
  body {
    background: var(--backdrop);
    font-family: "Arimo", Arial, sans-serif;
    color: var(--ink);
    position: relative;
  }
  .sheet {
    position: absolute;
    background: var(--paper);
    box-shadow: 0 2px 8px rgba(0,0,0,0.12);
    overflow: hidden;
  }
  .edge-tab {
    position: absolute;
    width: 8px;
    background: linear-gradient(180deg, var(--brand-blue), var(--brand-blue-deep));
  }
  .brand {
    position: absolute;
    display: flex;
    align-items: center;
    gap: 10px;
  }
  .brand-mark {
    width: 34px; height: 34px;
    background: var(--brand-blue);
    flex: none;
  }
  .brand-name {
    font-weight: 700;
    color: var(--ink);
    font-size: 17px;
    line-height: 1.1;
    text-transform: uppercase;
    letter-spacing: 0.2px;
    white-space: nowrap;
  }
  .brand-tagline {
    position: absolute;
    font-size: 10px;
    font-weight: 700;
    color: var(--ink-soft);
    white-space: nowrap;
  }
  .contact {
    position: absolute;
    font-size: 10px;
    line-height: 1.45;
    color: var(--ink-soft);
    white-space: nowrap;
  }
  .contact b { color: var(--ink); }
  .decor {
    position: absolute;
    border-radius: 24px;
    background: radial-gradient(ellipse at center, var(--brand-blue-pale), rgba(214,240,248,0));
  }

  /* Letterhead */
  .letterhead { left: 240px; top: 60px; width: 588px; height: 720px; }
  .letterhead .brand { left: 26px; top: 28px; }
  .letterhead .brand-tagline { left: 70px; top: 74px; }
  .letterhead .contact { left: 370px; top: 30px; }
  .letterhead .edge-tab { right: 0; top: 14px; height: 48px; }
  .letterhead .decor { left: 180px; top: 300px; width: 150px; height: 140px; }

  /* Business card front */
  .card { border-radius: 16px; }
  .card-front { left: 48px; top: 173px; width: 341px; height: 211px; }
  .card-front .brand { left: 24px; top: 24px; }
  .card-front .brand-tagline { left: 134px; top: 82px; }
  .card-holder {
    position: absolute; right: 190px; top: 124px; text-align: right;
  }
  .card-holder .person { font-size: 12px; font-weight: 700; color: var(--brand-blue-deep); white-space: nowrap; }
  .card-holder .role { font-size: 8.5px; font-weight: 700; color: var(--ink); margin-top: 2px; }
  .card-front .contact { left: 160px; top: 112px; font-size: 8px; }
  .card-front .tab-left { left: 0; top: 112px; height: 44px; }
  .card-front .tab-right { right: 0; top: 112px; height: 44px; }

  /* Business card back */
  .card-back { left: 48px; top: 396px; width: 341px; height: 187px; }
  .card-back .brand { left: 60px; top: 38px; }
  .card-back .brand-tagline { left: 160px; top: 96px; }
  .card-back .web {
    position: absolute; left: 0; right: 0; bottom: 24px;
    text-align: center; font-size: 10px; color: var(--ink);
  }

  /* Envelope */
  .envelope { left: 540px; top: 336px; width: 619px; height: 444px; }
  .envelope .flap { position: absolute; left: 0; top: 0; }
  .envelope .brand { left: 24px; top: 128px; }
  .envelope .brand-tagline { left: 68px; top: 174px; }
  .envelope .contact { left: 14px; top: 314px; }
  .envelope .edge-tab { left: 0; top: 308px; height: 56px; }
  .envelope .decor { right: 20px; bottom: 20px; width: 170px; height: 150px; }
  .envelope .flap-decor { left: 270px; top: 8px; width: 90px; height: 70px; }
</style>
</head>
<body>

  <section class="sheet letterhead" aria-label="Letterhead">
    <div class="brand">
      <span class="brand-mark"></span>
      <span class="brand-name">Vellmore Quadrant<br>Systems LLC</span>
    </div>
    <div class="brand-tagline">Elevate Your Workflow</div>
    <div class="contact">
      Brennick, VA<br>
      <b>Cell :</b> 202.555.0147<br>
      <b>Email :</b> dorian@vellmore-quadrant.example<br>
      <b>Web :</b> www.vellmore-quadrant.example
    </div>
    <span class="edge-tab"></span>
    <div class="decor" role="img" aria-label="Faint brand watermark decoration"></div>
  </section>

  <section class="sheet card card-front" aria-label="Business card front">
    <div class="brand">
      <span class="brand-mark"></span>
      <span class="brand-name">Vellmore Quadrant<br>Systems LLC</span>
    </div>
    <div class="brand-tagline">Elevate Your Workflow</div>
    <div class="card-holder">
      <div class="person">Dorian Feltcher</div>
      <div class="role">President</div>
    </div>
    <div class="contact">
      Brennick, VA<br>
      <b>Cell :</b> 202.555.0147<br>
      <b>Email :</b> dorian@vellmore-quadrant.example<br>
      <b>Web :</b> www.vellmore-quadrant.example
    </div>
    <span class="edge-tab tab-left"></span>
    <span class="edge-tab tab-right"></span>
  </section>

  <section class="sheet card card-back" aria-label="Business card back">
    <div class="brand">
      <span class="brand-mark"></span>
      <span class="brand-name">Vellmore Quadrant<br>Systems LLC</span>
    </div>
    <div class="brand-tagline">Elevate Your Workflow</div>
    <div class="web">www.vellmore-quadrant.example</div>
  </section>

  <section class="sheet envelope" aria-label="Envelope">
    <svg class="flap" width="619" height="120" viewBox="0 0 619 120" aria-hidden="true">
      <defs>
        <linearGradient id="flap-fill" x1="0" y1="0" x2="0" y2="1">
          <stop offset="0" stop-color="#9fdcef"/>
          <stop offset="1" stop-color="#1ea9d3"/>
        </linearGradient>
      </defs>
      <path d="M0 0 H619 V44 Q310 118 0 44 Z" fill="url(#flap-fill)"/>
      <path d="M0 44 Q310 118 619 44" fill="none" stroke="#0d8fbb" stroke-width="3"/>
    </svg>
    <div class="decor flap-decor" role="img" aria-label="Brand decoration on envelope flap"></div>
    <div class="brand">
      <span class="brand-mark"></span>
      <span class="brand-name">Vellmore Quadrant<br>Systems LLC</span>
    </div>
    <div class="brand-tagline">Elevate Your Workflow</div>
    <div class="contact">
      Brennick, VA<br>
      <b>Cell :</b> 202.555.0147<br>
      <b>Email :</b> dorian@vellmore-quadrant.example<br>
      <b>Web :</b> www.vellmore-quadrant.example
    </div>
    <span class="edge-tab"></span>
    <div class="decor" role="img" aria-label="Faint brand watermark decoration"></div>
  </section>

</body>
</html>
```